Tevrix BIM business website

I have a logo design and business card concept is ongoing at this point, but i need a website design based on VDC or BIM ("Virtual Building and Construction" or "Building Information Modeling") that will stand out for the quality and concept that we provide. I am a consultant providing training and production work for Quorvel (Zembrick application <where most of the overview can be obtained>). We are providing BIM production and coordination services as well. I can fill in the meat but I need an open development website. Currently, just obtaining a domain so it can be included on a business card is the quickest objective, then developing the content and launching it.

Business

```html
<!DOCTYPE html>
<html lang="en">
<head>
<meta charset="utf-8">
<title>Tevrix BIM Consulting</title>
<link href="https://fonts.googleapis.com/css2?family=Roboto:wght@300;400;500;700&display=swap" rel="stylesheet">
<style>
:root{
  --navy:#1f2a5a;
  --navy-text:#1c2556;
  --orange:#f5a623;
  --blue:#4187c6;
  --grey-panel:#f1f2f4;
  --text:#8a8a8a;
  --text-dark:#333;
  --line:#dcdcdc;
  --white:#fff;
}
*{box-sizing:border-box;margin:0;padding:0}
html,body{width:1200px;height:2329px;overflow:hidden;background:var(--white);font-family:'Roboto',sans-serif}
.page{position:relative;width:1200px;height:2329px}
.abs{position:absolute}

/* Hero */
.hero{position:absolute;left:0;top:0;width:1200px;height:564px;background:var(--navy)}
.hero-art{position:absolute;left:372px;top:186px;width:746px;height:378px;
  background:radial-gradient(ellipse at 65% 45%,rgba(60,170,200,.55),rgba(40,110,170,.25) 45%,rgba(31,42,90,0) 72%)}
.brand{position:absolute;left:52px;top:44px;display:flex;align-items:center;gap:10px}
.brand-dot{width:34px;height:34px;border-radius:50%;background:var(--orange)}
.brand-name{font-size:30px;font-weight:700;color:var(--white)}
.socials{position:absolute;top:56px;left:790px;display:flex;gap:14px}
.socials span{width:14px;height:14px;border-radius:50%;background:var(--white)}
.call-top{position:absolute;left:955px;top:51px;font-size:19px;font-weight:500;color:var(--white)}
.nav{position:absolute;top:107px;left:0;font-size:13px;color:var(--white)}
.nav a{position:absolute;white-space:nowrap;color:var(--white);text-decoration:none}
.nav .active{color:var(--orange);left:514px;width:70px;text-align:center;border-left:1px solid var(--orange);border-right:1px solid var(--orange);height:18px}
.btn{display:flex;align-items:center;justify-content:center;border:1px solid var(--orange);border-radius:20px;color:var(--orange);font-size:13px}
.btn-consult{position:absolute;left:1026px;top:96px;width:123px;height:39px}
.hero-title{position:absolute;left:152px;top:300px;font-size:33px;line-height:41px;font-weight:700;color:var(--white)}
.btn-hero{position:absolute;left:152px;top:461px;width:121px;height:39px}
.dots{position:absolute;left:947px;top:476px;display:flex;gap:12px}
.dots span{width:5px;height:5px;background:var(--white);opacity:.8}
.dots span:first-child{background:var(--orange)}

/* About */
.about-panel{position:absolute;left:765px;top:564px;width:435px;height:484px;background:var(--grey-panel)}
.about-art{position:absolute;left:629px;top:652px;width:473px;height:334px;
  background:linear-gradient(135deg,#e9e9e9,#cfcfcf 55%,#c9463f 56%,#b9b9b9 62%,#ececec)}
.eyebrow{position:absolute;left:152px;top:643px;font-size:13px;color:var(--orange)}
.about-title{position:absolute;left:152px;top:692px;font-size:23px;font-weight:500;color:var(--navy-text)}
.about-lead{position:absolute;left:152px;top:736px;width:430px;font-size:19px;font-weight:300;line-height:24px;color:var(--text)}
.about-copy{position:absolute;left:152px;top:825px;width:440px;font-size:12.5px;line-height:18px;color:var(--text)}
.more-link{position:absolute;left:152px;top:954px;font-size:13px;color:var(--navy-text)}

/* Services */
.services{position:absolute;left:0;top:1048px;width:1200px;height:602px;background:var(--blue)}
.section-title{position:absolute;left:0;width:1200px;text-align:center;font-size:23px;font-weight:500}
.section-sub{position:absolute;left:0;width:1200px;text-align:center;font-size:12.5px}
.service{position:absolute;top:1200px;width:283px}
.service-photo{width:283px;height:202px}
.service-name{margin-top:20px;font-size:15px;font-weight:500;color:var(--white)}
.service-copy{margin-top:6px;font-size:12.5px;line-height:18px;color:var(--white)}
.service .btn{margin-top:18px;width:121px;height:38px}
.service .btn.filled{background:var(--orange);color:var(--white)}

/* Testimonials */
.review{position:absolute;top:1824px;width:435px;height:171px;border:1px solid #eee;padding:48px 26px 0 26px}
.avatar{position:absolute;left:26px;top:-28px;width:54px;height:54px;border-radius:50%;background:#3a3a3a}
.review-name{font-size:15px;font-weight:500;color:var(--text-dark)}
.review-name small{font-size:10px;font-weight:400;color:#aaa}
.review-copy{margin-top:8px;font-size:12.5px;line-height:18px;color:var(--text)}
.arrow{position:absolute;top:1897px;width:24px;height:24px;border-radius:50%;border:1px solid #e4e4e4}
.arrow.next{border:2px solid var(--orange)}

/* Footer */
.footer-line{position:absolute;left:51px;top:2075px;width:1098px;height:1px;background:var(--line)}
.copy{position:absolute;left:76px;top:2153px;font-size:12.5px;color:var(--text-dark)}
.foot-brand{position:absolute;left:76px;top:2176px;font-size:19px;color:#aaa}
.foot-brand b{color:var(--navy-text);font-weight:700}
.reserved{position:absolute;left:76px;top:2216px;font-size:11px;color:#bbb}
.foot-links{position:absolute;top:2151px;font-size:12.5px;line-height:21px;color:var(--text)}
.foot-call{position:absolute;left:893px;top:2151px;font-size:19px;color:#666}
.foot-mail{position:absolute;left:893px;top:2180px;font-size:11px;color:#666}
.foot-social{position:absolute;left:893px;top:2226px;display:flex;gap:17px}
.foot-social span{width:13px;height:13px;border-radius:50%;background:#bbb}
.foot-social span:nth-child(2){background:var(--orange)}
</style>
</head>
<body>
<div class="page">

<header class="hero">
  <div class="hero-art" role="img" aria-label="Glowing wireframe of a building under construction with floating fragments"></div>
  <div class="brand"><span class="brand-dot"></span><span class="brand-name">Tevrix</span></div>
  <div class="socials" aria-label="Social links"><span></span><span></span><span></span><span></span></div>
  <div class="call-top">Call Us: 800-555-0142</div>
  <nav class="nav">
    <a class="active">Home</a>
    <a style="left:621px">Our Story</a>
    <a style="left:711px">Service</a>
    <a style="left:788px">Testimonials</a>
    <a style="left:899px">Contact Us</a>
  </nav>
  <div class="btn btn-consult">Consult Now</div>
  <h1 class="hero-title">Building Information<br>Modeling BIM and Virtual<br>Construction</h1>
  <div class="btn btn-hero">Explore More</div>
  <div class="dots"><span></span><span></span><span></span><span></span><span></span></div>
</header>

<section class="about">
  <div class="about-panel"></div>
  <div class="about-art" role="img" aria-label="Sketch of a building model cut open with red highlighted walls over blueprints"></div>
  <div class="eyebrow">About Us</div>
  <h2 class="about-title">Tevrix BIM Consulting</h2>
  <p class="about-lead">I am a consultant provid training &amp; production work for Quorvel (Zembrick application, where most of the overview can be obtained</p>
  <p class="about-copy">Lorem Ipsum is simply dummy text of the printing and typesetting industry. Lorem Ipsum has been the industry's standard dummy text ever since the 1500s, when an unknown printer took a galley of type and scrambled it to make a type specimen book. It has survived not ...</p>
  <div class="more-link">More About Us &nbsp;→</div>
</section>

<section class="services">
  <h2 class="section-title" style="top:78px;color:var(--white)">Services we offer</h2>
  <p class="section-sub" style="top:107px;color:var(--white)">Lorem Ipsum has been the industry's standard dummy text ever</p>
</section>
<div class="service" style="left:152px">
  <div class="service-photo" role="img" aria-label="Consultants working together at a computer" style="background:linear-gradient(135deg,#dfe3e8,#8a8f99 60%,#c9ccd2)"></div>
  <h3 class="service-name">Providing Training</h3>
  <p class="service-copy">It is a long established fact that a reader will be distracted by the readable content of a page when looking at its layout.</p>
  <div class="btn filled">Explore More</div>
</div>
<div class="service" style="left:459px">
  <div class="service-photo" role="img" aria-label="Abstract blue and glass architectural model" style="background:linear-gradient(135deg,#eef0f3,#8ea6cf 55%,#3456a8 70%,#e3e6ea)"></div>
  <h3 class="service-name">Production work for Quorvel</h3>
  <p class="service-copy">It is a long established fact that a reader will be distracted by the readable content of a page when looking at its layout.</p>
  <div class="btn">Explore More</div>
</div>
<div class="service" style="left:765px">
  <div class="service-photo" role="img" aria-label="Red transparent building model on construction plans" style="background:linear-gradient(135deg,#e6e6e6,#d65050 50%,#b52a2a 60%,#dcdcdc)"></div>
  <h3 class="service-name">BIM production &amp; Coordination</h3>
  <p class="service-copy">It is a long established fact that a reader will be distracted by the readable content of a page when looking at its layout.</p>
  <div class="btn">Explore More</div>
</div>

<section class="testimonials">
  <h2 class="section-title" style="top:1716px;color:var(--navy-text)">Testimonials</h2>
  <p class="section-sub" style="top:1751px;color:#666">See what out client say about us</p>
  <div class="arrow" style="left:90px"></div>
  <div class="review" style="left:152px">
    <div class="avatar" role="img" aria-label="Client portrait"></div>
    <div class="review-name">Miles Corden, <small>CEO@Norvane Inc</small></div>
    <p class="review-copy">Lorem Ipsum has been the industry's standard dummy text ever since the 1500s, when an unknown printer took a galley of type and scrambled it to make a type specimen book ...</p>
  </div>
  <div class="review" style="left:612px">
    <div class="avatar" role="img" aria-label="Client portrait"></div>
    <div class="review-name">Lena Varsko, <small>Management@Pellora</small></div>
    <p class="review-copy">Lorem Ipsum has been the industry's standard dummy text ever since the 1500s, when an unknown printer took a galley of type and scrambled it to make a type specimen book ...</p>
  </div>
  <div class="arrow next" style="left:1085px"></div>
</section>

<footer>
  <div class="footer-line"></div>
  <div class="copy">Copyright © 2017</div>
  <div class="foot-brand"><b>Tevrix</b> Bim Consulting</div>
  <div class="reserved">All right reserved.</div>
  <div class="foot-links" style="left:459px">Our Story<br>Service<br>Testimonials<br>Contact Us<br>Sitemap</div>
  <div class="foot-links" style="left:664px">Term &amp; Condition<br>Policy<br>Help</div>
  <div class="foot-call">Call Us: (555) 310-4826</div>
  <div class="foot-mail">E : hello@tevrixbim.com</div>
  <div class="foot-social" aria-label="Social links"><span></span><span></span><span></span><span></span></div>
</footer>

</div>
</body>
</html>
```